Copper Gate Labradoodle web design

We're a new labradoodle breeder in Charleston, SC in need of a web design.

Our name is Copper Gate Labradoodles.

Site we like: http://www.fernhilldoodlery.example/
http://www.quailbrookpups.example/

Logo Font:
The ''Copper Gate'' font is called TestarossaNF and is available freely at http://www.typequarry.example/testarossa-nf.font.  The ''Labradoodles'' font is called Worstveld Sling Extra and is available freely at http://www.glyphbarn.example/WorstveldSlingExtra.php.

Requirements
Must have
• Our logo
1. Home page
2. Labradoodle F.A.Q.
3. Our doodles
4. Availability
5. Adoption Process
6. Contact us
Link/badge icon for Health Guarantee
Nice to have
• Color and font to match the logo.

An area to add pictures
Should not have
• Rainbows
Rainbow colors

```html
<!DOCTYPE html>
<html lang="en">
<head>
<meta charset="utf-8">
<title>Copper Gate Labradoodles</title>
<link rel="stylesheet" href="https://fonts.googleapis.com/css2?family=Federant&family=Titillium+Web:wght@300;400;600&display=swap">
<style>
:root{
  --pink:#e2566f;
  --pink-dark:#c9465e;
  --brown:#6a4a2c;
  --tan:#dcc1a2;
  --tan-dark:#a88a68;
  --text:#6b6b6b;
  --band:#3c3c3c;
  --footer:#5d5d5d;
  --footer-text:#f2f2f2;
  --rule:#d6d6d6;
  --page:#ffffff;
  --hero-top:#dcdcdc;
  --gold:#d4a62a;
}
*{box-sizing:border-box;margin:0;padding:0}
html,body{width:1200px;height:909px;overflow:hidden}
body{position:relative;background:var(--page);font-family:"Titillium Web",sans-serif;color:var(--text)}
.abs{position:absolute}
.hero-bg{left:0;top:0;width:1200px;height:400px;background:linear-gradient(180deg,var(--hero-top) 0%,#ececec 55%,var(--page) 100%)}
.grass{left:632px;top:0;width:448px;height:120px;border-radius:0 0 50% 50%;background:radial-gradient(ellipse at 50% 20%,#8fb43a 0%,#a9c75a 45%,rgba(169,199,90,0) 75%)}
.top-band{left:0;top:38px;width:1200px;height:48px;background:linear-gradient(180deg,#4a4a4a,var(--band) 60%,#2f2f2f)}
.brand-mark{left:192px;top:2px;width:120px;height:120px;border-radius:50%;background:#f3e6d6;border:5px solid var(--pink)}
.brand-name{left:322px;top:50px;font-family:"Titillium Web",sans-serif;font-weight:600;font-size:19px;color:#f3e6d6;white-space:nowrap}
.nav{left:570px;top:51px;height:26px}
.nav a{position:absolute;top:0;height:26px;line-height:26px;border-radius:13px;background:var(--pink);color:#fff;text-decoration:none;text-align:center;font-family:"Federant",serif;font-size:11px;letter-spacing:.2px;box-shadow:inset 0 -2px 0 var(--pink-dark)}
.hero-title{left:196px;top:160px;font-family:"Federant",serif;font-size:42px;line-height:42px;color:var(--pink);font-variant:small-caps}
.hero-sub{left:196px;top:264px;font-family:"Federant",serif;font-style:italic;font-size:18px;color:var(--pink);font-variant:small-caps}
.hero-copy{left:196px;top:288px;width:320px;font-size:9px;line-height:11.6px;color:#555}
.btn{display:block;height:24px;line-height:24px;text-align:center;background:var(--tan);color:var(--brown);font-family:"Federant",serif;font-style:italic;font-size:12px;text-decoration:none;border-radius:2px;box-shadow:0 3px 0 #cfcfcf;border-bottom:1px solid var(--tan-dark)}
.hero-photo{left:704px;top:132px;width:156px;height:244px;border-radius:45% 45% 20% 20%;background:radial-gradient(ellipse at 50% 40%,#c98d55 0%,#b77a43 55%,rgba(183,122,67,0) 80%)}
.dots{left:936px;top:367px}
.dots span{position:absolute;top:0;width:12px;height:12px;border-radius:50%;background:#cfcfcf}
.dots span.on{background:var(--pink)}
.col-title{font-family:"Federant",serif;font-size:20px;line-height:24px;color:var(--brown);font-variant:small-caps}
.benefits{left:198px;top:434px;width:200px}
.benefit-list{list-style:none;margin-top:12px;width:164px}
.benefit-list li{position:relative;padding:2px 0 4px 15px;font-size:10.5px;line-height:13.6px;color:#666;border-bottom:1px dotted var(--rule);margin-bottom:5px}
.benefit-list li:last-child{border-bottom:none}
.benefit-list li::before{content:"";position:absolute;left:0;top:6px;width:7px;height:7px;border-radius:50%;background:var(--pink)}
.v-rule{width:0;border-left:1px dotted #cfcfcf}
.welcome{left:455px;top:434px;width:230px}
.welcome p{margin-top:12px;font-size:10.5px;line-height:13.4px;font-weight:300;color:#666}
.principles{left:750px;top:438px;width:250px}
.principle{position:relative;padding-left:24px;margin-bottom:12px}
.principle::before{content:"";position:absolute;left:0;top:3px;width:14px;height:14px;border-radius:50%;background:var(--pink)}
.principle h3{font-family:"Federant",serif;font-weight:400;font-size:14px;line-height:18px;color:var(--brown);font-variant:small-caps}
.principle p{font-size:10.5px;line-height:13.4px;font-weight:300;color:#666;margin-top:2px}
.badge{left:932px;top:680px;width:62px;height:62px;border-radius:50%;background:radial-gradient(circle,#3a3a3a 0 52%,var(--gold) 54% 100%);box-shadow:0 1px 2px rgba(0,0,0,.3)}
.footer{left:0;top:726px;width:1200px;height:183px;background:var(--footer);color:var(--footer-text)}
.f-title{font-family:"Federant",serif;font-size:18px;color:#fff;font-variant:small-caps}
.f-copy{font-size:9px;line-height:11.6px}
.f-links{list-style:none}
.f-links li{font-size:11px;line-height:14px;padding:1px 0 5px;border-bottom:1px dotted #7c7c7c;width:125px;margin-bottom:2px}
.social{position:absolute;top:0;width:26px;height:26px;border-radius:50%;background:var(--pink);display:block}
.newsletter-label{font-size:15px;color:#fff}
.field-hint{font-size:9px;color:#9a9a9a;letter-spacing:.2px}
.email-field{width:146px;height:19px;background:#fff;border:none;box-shadow:inset 0 1px 2px rgba(0,0,0,.3)}
.send{width:46px;height:19px;background:var(--pink);color:#fff;font-size:10px;line-height:19px;text-align:center}
.f-contact p{font-size:11px;line-height:14.6px}
.copyright{left:0;top:885px;width:1200px;text-align:center;font-size:8.6px;color:#f0f0f0}
</style>
</head>
<body>
  <div class="abs hero-bg"></div>
  <div class="abs grass" role="img" aria-label="Tuft of green grass blades"></div>
  <div class="abs top-band"></div>

  <div class="abs brand-mark"></div>
  <div class="abs brand-name">Copper Gate Labradoodles</div>

  <nav class="abs nav">
    <a href="#" style="left:0;width:127px">OUR LABRADOODLES</a>
    <a href="#" style="left:136px;width:65px">AVAILABLE</a>
    <a href="#" style="left:210px;width:66px">PROGRAM</a>
    <a href="#" style="left:284px;width:66px">PROCESS</a>
    <a href="#" style="left:359px;width:66px">CONTACT</a>
  </nav>

  <h1 class="abs hero-title">Experience Love At<br>First Cuddle</h1>
  <h2 class="abs hero-sub">Why We are Different</h2>
  <p class="abs hero-copy">As premier Australian multi-gen labradoodle breeders in California, we take our labradoodle puppies seriously! Our dogs are a part of our family and live indoors. Every labradoodle puppy has completed health testing and we strive for proper temperament, ability and conformation.</p>
  <a class="abs btn" href="#" style="left:196px;top:350px;width:96px">Enquire Now</a>

  <div class="abs hero-photo" role="img" aria-label="Photo of a sitting apricot labradoodle puppy"></div>
  <div class="abs dots">
    <span class="on" style="left:0"></span><span style="left:16px"></span><span style="left:31px"></span><span style="left:47px"></span>
  </div>

  <section class="abs benefits">
    <h2 class="col-title">Benefits for the Pet</h2>
    <ul class="benefit-list">
      <li>24 Hour Contact with sitter.</li>
      <li>Provide documentation about daily activities with your pet.</li>
      <li>Give medication on time.</li>
      <li>Less stress being in their own quiet, familiar environment.</li>
      <li>Routine stays the same.</li>
      <li>Pet is not exposed to illnesses or fleas.</li>
      <li>Personal attention, love and affection.</li>
    </ul>
  </section>

  <div class="abs v-rule" style="left:425px;top:456px;height:192px"></div>

  <section class="abs welcome">
    <h2 class="col-title">Welcome Labradoodle Lovers</h2>
    <p>As multi-gen labradoodle breeders in California, we specialize in allergy-friendly, non-shedding Multigen Australian Labradoodles. We choose to breed just a few, select mini and medium labradoodle puppy litters each year. We offer lifetime support on all labradoodle puppies and you can be certain that our two little girls will properly socialize your labradoodle puppy before it's placed into your arms.<br>We have a whimsical, silly outlook on life and we like to think that our labradoodle dogs.</p>
  </section>
  <a class="abs btn" href="#" style="left:455px;top:648px;width:90px">Read More</a>

  <div class="abs v-rule" style="left:719px;top:456px;height:192px"></div>

  <section class="abs principles">
    <div class="principle">
      <h3>Our Principles</h3>
      <p>Our strong principles are the slogan of Bright Paw Pet Care. We deliver personable, expert services with a high degree of integrity.</p>
    </div>
    <div class="principle" style="margin-top:18px">
      <h3>Labradoodle Love</h3>
      <p>We are all God's creations. Pets need care and unconditional love.</p>
    </div>
    <div class="principle" style="margin-top:18px">
      <h3>Testimonials</h3>
      <p>If you are still on the fence, listen to the feedback of previous clients and what they thought of Bright Paw Pet Care.</p>
    </div>
  </section>
  <a class="abs btn" href="#" style="left:774px;top:648px;width:89px">Read More</a>

  <footer class="abs footer">
    <div class="abs" style="left:198px;top:22px;width:200px">
      <h2 class="f-title">Gallery</h2>
      <p class="f-copy" style="margin-top:8px">Much like our children, our pets are unique with their own personalities. We celebrate the uniqueness of all of our pets through an owner-inspired "growllerly". Enjoy!</p>
    </div>
    <a class="abs btn" href="#" style="left:197px;top:112px;width:95px">Enquire Now</a>

    <div class="abs v-rule" style="left:422px;top:26px;height:140px;border-color:#8a8a8a"></div>

    <div class="abs" style="left:451px;top:22px">
      <h2 class="f-title">Links</h2>
      <ul class="f-links" style="margin-top:8px">
        <li>Board of Directors</li>
        <li>Dog Park Rules</li>
        <li>Map</li>
        <li>Education</li>
      </ul>
    </div>

    <div class="abs v-rule" style="left:602px;top:26px;height:140px;border-color:#8a8a8a"></div>

    <div class="abs" style="left:630px;top:22px;width:200px;height:140px">
      <h2 class="f-title">Connect With Us</h2>
      <div class="abs" style="left:0;top:27px;width:100px;height:26px">
        <a class="social" href="#" style="left:0" aria-label="Social link one"></a>
        <a class="social" href="#" style="left:33px" aria-label="Social link two"></a>
        <a class="social" href="#" style="left:66px" aria-label="News feed"></a>
      </div>
      <p class="abs newsletter-label" style="left:0;top:64px">Newsletter</p>
      <p class="abs field-hint" style="left:0;top:85px">YOUR EMAIL ADDRESS</p>
      <div class="abs email-field" style="left:0;top:99px"></div>
      <div class="abs send" style="left:147px;top:99px">SEND</div>
    </div>

    <div class="abs v-rule" style="left:848px;top:26px;height:140px;border-color:#8a8a8a"></div>

    <div class="abs f-contact" style="left:878px;top:26px">
      <h2 class="f-title">Contact Us</h2>
      <div style="margin-top:6px">
        <p>Meeting St 48</p>
        <p>29401 Charleston</p>
        <p>South Carolina</p>
        <p>+1 843 555 0142</p>
        <p>info@coppergatedoodles.example</p>
      </div>
    </div>
  </footer>
  <p class="abs copyright">Copyright © 2012 ~ All Rights Reserved ~ We are proud to be a responsible California Multigen Labradoodle Puppy Breeder!</p>

  <a class="abs badge" href="#" aria-label="Health guarantee"></a>
</body>
</html>
```